MOSLEN Environmental needs an upgrade to its current business cards design

We need an upgrade to our current business cards design, where the MOSLEN acronym is included, as possible and not being overloaded.
MOSLEN Environmental is an Environmental Consultancy Firm based in Sydney.
We would like to see creative designs different from the standard type of business cards (for example, rounded edges, different to standard size of common business cards.

Target Market(s)

industrial companies (oil & gas, petrochemical, mining, insolvency, finance and manufacturing), developers, architect firms, law firms.

Industry/Entity Type

Business

Contact Information for Business Card

logos (brand and acronym), if they don't appear overloaded.
name
role
name of company (MOSLEN Environmental),
address (Level 3, Suite 3C, 47-49 Dorrigan Lane, Wexmoor, NSW, 2188) landline (02 7314 2986)
mobile (staff member)
email (staff member) and
website (www.moslengreen.example).
Include: Contaminated Land, Site Remediation, Groundwater Assessment, Health and Ecological Risk Assessments, Acid Sulfate Soils, Waste Classification.

Font styles to use
Serif
Sans Serif

Requirements
Must have
• A creative design different to the standard type of business cards.
Nice to have
• Rounded edges
• Different size of business cards rather than the standard size.
Should not have
• Preferable not to use white colour background, unless it is required from a creative design proposed.
• Not an overloaded design.
• Avoid black colours

```html
<!DOCTYPE html>
<html lang="en">
<head>
<meta charset="UTF-8">
<title>MOSLEN Environmental – Business Cards</title>
<link href="https://fonts.googleapis.com/css2?family=Montserrat:wght@500;600;700;800;900&display=swap" rel="stylesheet">
<style>
  :root {
    --backdrop: #1f5424;
    --brand-green: #3bb64b;
    --charcoal: #444446;
    --slate: #68686b;
    --ink-light: #ffffff;
  }
  * { margin: 0; padding: 0; box-sizing: border-box; }
  html, body {
    width: 1200px; height: 900px; overflow: hidden;
    background: var(--backdrop);
    font-family: "Montserrat", Arial, sans-serif;
    color: var(--ink-light);
  }
  .canvas { position: relative; width: 1200px; height: 900px; }

  .card {
    position: absolute;
    width: 560px; height: 320px;
    border-radius: 28px;
    overflow: hidden;
    background: var(--brand-green);
    box-shadow: 0 10px 24px rgba(0,0,0,0.28);
  }
  .card--front { left: 60px; top: 110px; }
  .card--back  { left: 580px; top: 470px; }

  /* Wordmark */
  .wordmark { position: absolute; text-align: center; font-weight: 800; line-height: 1; }
  .wordmark__name { display: block; letter-spacing: 1px; }
  .wordmark__sub { display: block; letter-spacing: 4px; }

  .card--front .wordmark { left: 0; right: 0; top: 92px; }
  .card--front .wordmark__name { font-size: 62px; }
  .card--front .wordmark__sub { font-size: 17px; margin-top: 6px; }

  .services {
    position: absolute; left: 26px; bottom: 30px;
    font-size: 10.2px; font-weight: 700; line-height: 1.45;
    white-space: nowrap;
  }

  /* Back card */
  .back-shapes { position: absolute; inset: 0; }
  .card--back .wordmark { left: 40px; top: 128px; width: 260px; }
  .card--back .wordmark__name { font-size: 42px; }
  .card--back .wordmark__sub { font-size: 12px; margin-top: 5px; letter-spacing: 3px; }

  .contact { position: absolute; left: 372px; top: 42px; }
  .contact__name { font-size: 22px; font-weight: 700; line-height: 1.1; }
  .contact__role { font-size: 10.5px; font-weight: 600; letter-spacing: 0.5px; margin-bottom: 16px; }
  .contact__list { list-style: none; }
  .contact__item {
    display: flex; align-items: flex-start; gap: 9px;
    font-size: 10px; font-weight: 500; line-height: 1.45; margin-bottom: 7px;
    letter-spacing: 0.3px;
  }
  .contact__icon { width: 12px; height: 12px; flex: none; margin-top: 1px; fill: var(--ink-light); }
</style>
</head>
<body>
<main class="canvas">

  <section class="card card--front" aria-label="Card front">
    <div class="wordmark">
      <span class="wordmark__name">MOSLEN</span>
      <span class="wordmark__sub">ENVIRONMENTAL</span>
    </div>
    <p class="services">
      Contaminated Land • Site Remediation • Groundwater Assessment<br>
      Health and Ecological Risk Assessments • Acid Sulfate Soils • Waste Classification
    </p>
  </section>

  <section class="card card--back" aria-label="Card back">
    <svg class="back-shapes" viewBox="0 0 560 320" width="560" height="320" aria-hidden="true">
      <path d="M0 0 H238 C350 60 392 210 356 320 H0 Z" fill="var(--slate)"/>
      <path d="M0 0 H214 C330 62 372 210 334 320 H0 Z" fill="var(--charcoal)"/>
    </svg>

    <div class="wordmark">
      <span class="wordmark__name">MOSLEN</span>
      <span class="wordmark__sub">ENVIRONMENTAL</span>
    </div>

    <div class="contact">
      <p class="contact__name">Aaron Pell</p>
      <p class="contact__role">Managing Director</p>
      <ul class="contact__list">
        <li class="contact__item">
          <svg class="contact__icon" viewBox="0 0 12 12" aria-hidden="true"><path d="M2.2 0.8 L4 0.5 L5 3 L3.8 4 C4.4 5.5 5.8 7 7.5 7.9 L8.6 6.8 L11.2 7.8 L11 9.6 C10.8 10.8 9.8 11.4 8.6 11.1 C4.6 10 1.6 7 0.7 3.3 C0.4 2 1 1 2.2 0.8 Z"/></svg>
          <span>02 7314 2986</span>
        </li>
        <li class="contact__item">
          <svg class="contact__icon" viewBox="0 0 12 12" aria-hidden="true"><rect x="3" y="0.5" width="6" height="3" rx="0.5"/><rect x="0.5" y="4" width="11" height="5" rx="1"/><rect x="3" y="8" width="6" height="3.5" rx="0.5"/></svg>
          <span>0412 558 903</span>
        </li>
        <li class="contact__item">
          <svg class="contact__icon" viewBox="0 0 12 12" aria-hidden="true"><path d="M0.5 2 H11.5 V10 H0.5 Z M1.6 3 V9 H10.4 V3 L6 6.4 Z M2.2 3 L6 5.6 L9.8 3 Z" fill-rule="evenodd"/></svg>
          <span>aaron@moslengreen.example</span>
        </li>
        <li class="contact__item">
          <svg class="contact__icon" viewBox="0 0 12 12" aria-hidden="true"><circle cx="6" cy="6" r="5.5"/><path d="M3 4 C4.5 3 5 5 6.5 4.5 C7.5 6 5 7 6 9 C4.5 9 3 7 3 4 Z" fill="var(--brand-green)"/></svg>
          <span>www.moslengreen.example</span>
        </li>
        <li class="contact__item">
          <svg class="contact__icon" viewBox="0 0 12 12" aria-hidden="true"><path d="M6 0.5 C8.3 0.5 10 2.2 10 4.4 C10 7.2 6 11.5 6 11.5 C6 11.5 2 7.2 2 4.4 C2 2.2 3.7 0.5 6 0.5 Z M6 2.8 A1.6 1.6 0 1 0 6 6 A1.6 1.6 0 1 0 6 2.8 Z" fill-rule="evenodd"/></svg>
          <span>Level 3, Suite 3C, 47-49 Dorrigan Lane,<br>Wexmoor, NSW, 2188</span>
        </li>
      </ul>
    </div>
  </section>

</main>
</body>
</html>
```